The Bright Lantern, an online college fair for non-traditional students, needs a web site

I need design and coding for a functioning web site that will serve as an online college fair that connects non-traditional students with college admissions officers and college advisors. I have chosen Wordpress and the "Meridian" theme for the site, and you can see what I already have here: https://brightlanternhub.example/
I need help setting up the site's pages and functionality, including SEO optimization and a password protected area. I will manage all content. In addition to me as the administrator, other users will be: college admissions officers, non-traditional students (like homeschoolers), and college advisors.
Target Market(s)
Homeschoolers and college/university admissions officers
Industry/Entity Type
College
Coding
Coded - Design and coding required
Number of Pages Required
5+ page
Font styles to use
Requirements
Must have
- - An inviting but professional look (see the logo as a starting point)
- - Easy to navigate
- - A way to register subscribed members (students)
- - A password-protected "members only" area
- - Virtual "booths" on the Schools page that lead to a detail page for each school
- - SEO optimized
Nice to have
- - Searchable site

```html
<!DOCTYPE html>
<html lang="en">
<head>
<meta charset="utf-8">
<title>The Bright Lantern – A Virtual College Fair for Non-Traditional Students</title>
<link rel="stylesheet" href="https://fonts.googleapis.com/css2?family=Open+Sans:wght@400;600;700;800&display=swap">
<style>
:root{
  --red:#d8310b;
  --red-dark:#b52708;
  --ink:#1b1b1b;
  --text:#333;
  --grey-band:#d1cfcf;
  --nav:#8b8685;
  --dark-btn:#454545;
  --white:#fff;
  --hero-a:#2a1f18;
  --hero-b:#4b3524;
}
*{box-sizing:border-box;margin:0;padding:0}
html,body{width:1200px;height:2597px;overflow:hidden}
body{position:relative;background:var(--white);font-family:"Open Sans",Arial,sans-serif;color:var(--text)}
.abs{position:absolute}
.login{left:990px;top:9px;width:123px;height:34px;background:var(--red);color:var(--white);font-size:13px;display:flex;align-items:center;justify-content:center}
.nav{left:0;top:54px;width:1200px;height:38px;background:var(--nav);display:flex;justify-content:center;gap:0}
.nav a{color:var(--white);text-decoration:none;font-size:13.5px;font-weight:600;padding:0 22px;line-height:38px;position:relative}
.nav a.active::after{content:"";position:absolute;left:22px;right:22px;bottom:0;height:3px;background:var(--red)}
.hero{left:0;top:92px;width:1200px;height:476px;background:radial-gradient(ellipse at 50% 30%,#6b4a30 0%,var(--hero-b) 35%,var(--hero-a) 100%)}
.brand{left:0;width:1200px;top:236px;text-align:center;color:var(--white);font-weight:700;font-size:38px;letter-spacing:2px;text-transform:uppercase}
.tagline{left:0;width:1200px;top:313px;text-align:center;color:var(--white);font-weight:600;font-size:14px}
.search{left:352px;top:378px;width:496px;height:38px;background:var(--white);border-radius:19px}
.search svg{position:absolute;right:14px;top:9px}
.h2{left:0;width:1200px;text-align:center;font-weight:700;font-size:26px;color:var(--ink);letter-spacing:1.5px}
.card{top:627px;width:315px;height:142px;background:var(--red);color:var(--white);font-size:22px;padding:16px 20px}
.card svg{position:absolute;right:26px;top:22px}
.photo{background:linear-gradient(160deg,#cfc8c2,#8d8582)}
.adv-name{font-weight:700;font-size:14px;letter-spacing:1.5px;color:var(--ink)}
.adv-role{font-size:10px;color:var(--red);font-weight:600}
.adv-social{font-size:10px;font-weight:700;color:var(--ink);display:flex;align-items:center;width:190px}
.adv-social .dots{margin-left:auto;display:flex;gap:9px}
.dot{width:9px;height:9px;border-radius:50%;background:var(--ink)}
.btn{height:38px;border-radius:19px;color:var(--white);font-size:13px;font-weight:700;display:flex;align-items:center;justify-content:center}
.btn.red{background:var(--red)}
.btn.dark{background:var(--dark-btn)}
.band{left:0;width:1200px;background:var(--grey-band)}
.schools-title{left:679px;top:1320px;font-size:25px;font-weight:700;color:var(--ink);letter-spacing:1px}
.schools-copy{left:679px;top:1376px;width:436px;font-size:12px;line-height:18px;color:var(--ink)}
.news-title{font-weight:700;font-size:14px;text-align:center;color:var(--ink);letter-spacing:.5px}
.news-copy{font-size:12.5px;text-align:center;line-height:18px;color:var(--ink)}
.news-meta{font-size:12px;color:var(--red);display:flex;align-items:center}
.news-meta .stats{margin-left:auto;display:flex;gap:10px;color:var(--ink);font-size:11px;align-items:center}
.newsletter-input{left:352px;top:2189px;width:496px;height:35px;background:var(--white);border-radius:18px;font-size:12px;color:#888;padding-left:12px;line-height:35px}
.newsletter-input svg{position:absolute;right:12px;top:11px}
.rule{left:87px;top:2263px;width:1026px;height:1px;background:var(--red)}
.foot-h{font-size:16px;font-weight:600;color:var(--ink);letter-spacing:.5px}
.about{left:87px;top:2311px;width:420px;font-size:12.5px;line-height:18px;color:var(--ink)}
.contact{left:87px;font-size:12.5px;color:var(--ink);display:flex;gap:14px;align-items:flex-start;line-height:18px}
.map{left:694px;top:2310px;width:419px;height:166px;background:linear-gradient(135deg,#cfdcae 0%,#e8e2c6 50%,#a9c4d8 100%)}
.socials{left:520px;top:2530px;width:160px;display:flex;justify-content:center;gap:20px;align-items:center}
.socials .c{width:22px;height:22px;border-radius:50%;background:var(--red)}
.copy{left:87px;top:2579px;font-size:11.5px;color:var(--ink)}
</style>
</head>
<body>

<header>
  <div class="abs login">LOG IN / SIGN UP</div>
  <nav class="abs nav">
    <a class="active">HOME</a><a>STUDENTS</a><a>SCHOOLS</a><a>ADVISORS</a><a>MEMBER RESOURSES</a><a>NEWS</a><a>CONTACT US</a>
  </nav>
</header>

<section>
  <div class="abs hero" role="img" aria-label="Dim library hall lined with tall wooden bookshelves"></div>
  <div class="abs brand">The Bright Lantern</div>
  <div class="abs tagline">A Virtual College Fair for Non-Traditional Students</div>
  <div class="abs search">
    <svg width="20" height="20" viewBox="0 0 20 20"><circle cx="8" cy="8" r="6" fill="none" stroke="#111" stroke-width="2.6"/><line x1="12.5" y1="12.5" x2="18.5" y2="18.5" stroke="#111" stroke-width="3" stroke-linecap="round"/></svg>
  </div>
</section>

<section>
  <h2 class="abs h2" style="top:580px">HOW IT WORKS</h2>
  <div class="abs card" style="left:87px">Courses
    <svg width="62" height="62" viewBox="0 0 62 62" fill="none" stroke="#fff" stroke-width="2.5"><rect x="17" y="2" width="26" height="26"/><rect x="3" y="32" width="26" height="26"/><rect x="33" y="32" width="26" height="26"/>
      <text x="30" y="23" fill="#fff" stroke="none" font-size="20" text-anchor="middle" font-family="Open Sans,sans-serif">A</text>
      <text x="16" y="53" fill="#fff" stroke="none" font-size="20" text-anchor="middle" font-family="Open Sans,sans-serif">B</text>
      <text x="46" y="53" fill="#fff" stroke="none" font-size="20" text-anchor="middle" font-family="Open Sans,sans-serif">C</text></svg>
  </div>
  <div class="abs card" style="left:443px">Apply Now
    <svg width="70" height="66" viewBox="0 0 70 66" fill="#fff"><path d="M48 2l14 14-30 30-18 4 4-18z"/><rect x="2" y="58" width="66" height="4"/></svg>
  </div>
  <div class="abs card" style="left:798px">Plan a Visit
    <svg width="62" height="64" viewBox="0 0 62 64" fill="#fff"><path d="M31 2l28 14H3z"/><rect x="6" y="20" width="50" height="4"/><rect x="10" y="28" width="5" height="24"/><rect x="21" y="28" width="5" height="24"/><rect x="36" y="28" width="5" height="24"/><rect x="47" y="28" width="5" height="24"/><rect x="4" y="55" width="54" height="6"/></svg>
  </div>
</section>

<section>
  <h2 class="abs h2" style="top:782px">FEATURED ADVISORS</h2>

  <div class="abs photo" style="left:87px;top:828px;width:263px;height:289px" role="img" aria-label="Portrait of a smiling advisor in a dark suit holding a folder"></div>
  <div class="abs adv-name" style="left:87px;top:1127px">DANA WHITFIELD</div>
  <div class="abs adv-role" style="left:87px;top:1146px">Multi Teacher</div>
  <div class="abs adv-social" style="left:87px;top:1165px">STAY CONNECTED<span class="dots"><i class="dot"></i><i class="dot"></i><i class="dot"></i></span></div>

  <div class="abs photo" style="left:469px;top:828px;width:264px;height:289px" role="img" aria-label="Portrait of a smiling advisor holding a red book in a library"></div>
  <div class="abs adv-name" style="left:469px;top:1127px">DANA WHITFIELD</div>
  <div class="abs adv-role" style="left:469px;top:1146px">Multi Teacher</div>
  <div class="abs adv-social" style="left:469px;top:1165px">STAY CONNECTED<span class="dots"><i class="dot"></i><i class="dot"></i><i class="dot"></i></span></div>

  <div class="abs photo" style="left:849px;top:828px;width:264px;height:289px" role="img" aria-label="Portrait of an advisor on the phone at a desk"></div>
  <div class="abs adv-name" style="left:849px;top:1127px">DANA WHITFIELD</div>
  <div class="abs adv-role" style="left:849px;top:1146px">Multi Teacher</div>
  <div class="abs adv-social" style="left:849px;top:1165px">STAY CONNECTED<span class="dots"><i class="dot"></i><i class="dot"></i><i class="dot"></i></span></div>

  <div class="abs btn red" style="left:452px;top:1195px;width:137px">Get in Touch</div>
  <div class="abs btn dark" style="left:615px;top:1195px;width:133px">All Advisors</div>
</section>

<section>
  <div class="abs band" style="top:1266px;height:353px"></div>
  <div class="abs" style="left:87px;top:1266px;width:531px;height:353px;background:linear-gradient(180deg,#9fb0c4 0%,#8d8676 45%,#5f7a3a 75%,#4f6e2c 100%)" role="img" aria-label="Students in red blazers walking across a lawn in front of a stone college building"></div>
  <div class="abs schools-title">FEATURED SCHOOLS</div>
  <p class="abs schools-copy">an audience of thousands of non-traditional students who want to hear about your school and programs. You will have a dedicated page to set up a virtual "booth", or school profile, where you can describe your institution, highlight aspects of your programs that may appeal to non-traditional students, offer details of their admissions process and requirements, and provide contact information for designated admissions representatives.</p>
  <div class="abs btn red" style="left:679px;top:1520px;width:133px">Get in Touch</div>
</section>

<section>
  <h2 class="abs h2" style="top:1647px">LATEST NEWS</h2>

  <div class="abs photo" style="left:87px;top:1688px;width:323px;height:272px" role="img" aria-label="Two students studying together at a library table"></div>
  <div class="abs news-title" style="left:87px;top:1966px;width:323px">CAMPUS NOTES</div>
  <p class="abs news-copy" style="left:87px;top:1991px;width:323px">freemembership for any student or parent who wants to learn more about the colleges and universities that are actively recruiting non-traditional students, all in one location!</p>
  <div class="abs news-meta" style="left:87px;top:2065px;width:323px">3rd November,2016<span class="stats"><span><span style="color:var(--red)">&#9829;</span> 18</span><span><span style="color:var(--red)">&#9632;</span> 2</span></span></div>

  <div class="abs photo" style="left:438px;top:1688px;width:324px;height:272px" role="img" aria-label="Student holding books in front of library shelves"></div>
  <div class="abs news-title" style="left:438px;top:1966px;width:324px">CAMPUS NOTES</div>
  <p class="abs news-copy" style="left:438px;top:1991px;width:324px">freemembership for any student or parent who wants to learn more about the colleges and universities that are actively recruiting non-traditional students, all in one location!</p>
  <div class="abs news-meta" style="left:438px;top:2065px;width:324px">3rd November,2016<span class="stats"><span><span style="color:var(--red)">&#9829;</span> 18</span><span><span style="color:var(--red)">&#9632;</span> 2</span></span></div>

  <div class="abs photo" style="left:790px;top:1688px;width:323px;height:272px" role="img" aria-label="Student with a tablet standing in a library"></div>
  <div class="abs news-title" style="left:790px;top:1966px;width:323px">CAMPUS NOTES</div>
  <p class="abs news-copy" style="left:790px;top:1991px;width:323px">freemembership for any student or parent who wants to learn more about the colleges and universities that are actively recruiting non-traditional students, all in one location!</p>
  <div class="abs news-meta" style="left:790px;top:2065px;width:323px">3rd November,2016<span class="stats"><span><span style="color:var(--red)">&#9829;</span> 18</span><span><span style="color:var(--red)">&#9632;</span> 2</span></span></div>
</section>

<footer>
  <div class="abs band" style="top:2104px;height:493px"></div>
  <h2 class="abs h2" style="top:2123px">NEWSLETTER</h2>
  <div class="abs newsletter-input">Enter your email address
    <svg width="16" height="12" viewBox="0 0 16 12"><rect width="16" height="12" fill="#d8310b"/><path d="M0 0l8 6 8-6" fill="none" stroke="#fff" stroke-width="1.4"/></svg>
  </div>
  <div class="abs rule"></div>

  <div class="abs foot-h" style="left:87px;top:2276px">ABOUT US</div>
  <p class="abs about">a platform for sharing your services and connecting with thousands of students who need your guidance. Through forums, articles, ads, and online events, there will be multiple opportunities to share your knowledge and expertise, and to work closely with individual students.</p>
  <div class="abs contact" style="top:2384px">
    <svg width="14" height="14" viewBox="0 0 14 14"><path d="M3 1l2.5 3-1.4 1.6a8 8 0 0 0 4.3 4.3L10 8.5l3 2.5-1.6 2A11 11 0 0 1 1 2.6z" fill="#d8310b"/></svg>+1 555 014 2281</div>
  <div class="abs contact" style="top:2415px">
    <svg width="14" height="11" viewBox="0 0 14 11"><rect width="14" height="11" fill="#d8310b"/><path d="M0 0l7 5.5L14 0" fill="none" stroke="#fff" stroke-width="1.3"/></svg>hello@brightlantern.example</div>
  <div class="abs contact" style="top:2446px">
    <svg width="14" height="18" viewBox="0 0 14 18"><path d="M7 0a7 7 0 0 1 7 7c0 5-7 11-7 11S0 12 0 7a7 7 0 0 1 7-7z" fill="#d8310b"/><circle cx="7" cy="7" r="2.5" fill="#d1cfcf"/></svg>
    <span>14 Harbor Lane,<br>Riverside Quarter</span></div>

  <div class="abs foot-h" style="left:694px;top:2276px">MAP</div>
  <div class="abs map" role="img" aria-label="Regional road map with a location marker"></div>

  <div class="abs socials">
    <i class="c"></i><i class="c"></i>
    <svg width="26" height="19" viewBox="0 0 26 19"><rect width="26" height="19" fill="#d8310b"/><path d="M0 0l13 10L26 0" fill="none" stroke="#d1cfcf" stroke-width="2"/></svg>
    <i class="c"></i>
  </div>
  <div class="abs copy">©brightlantern.All Rights Reserved.</div>
</footer>

</body>
</html>
```